Most captivating card ever!

Life Coach - Professional Adventurer - Entrepreneur
I need the worlds most amazing business card for my personal brand. This business card will mostly be used to give to prospective clients for life coaching and business coaching.
Be creative, be adventurous. It needs to stand out. Make people say.. I need this guy!
My background is as an entrepreneur and professional adventurer undertaking extreme expeditions. I am now moving into life coaching.
No specific design ideas, so you have full creativity. Show me your best.
Industry/Entity Type
Life Coaching
Contact Information for Business Card
Dan Pellow
itsdanp.com.au
0468215903
Colors
Designer to choose colors to be used in the design.
Look and feel

```html
<!DOCTYPE html>
<html lang="en">
<head>
<meta charset="utf-8">
<title>Business Card – Dan Pellow</title>
<link rel="stylesheet" href="https://fonts.googleapis.com/css2?family=Questrial&family=Source+Sans+3:wght@400&display=swap">
<style>
  :root {
    --backdrop: #2f434b;
    --backdrop-edge: #243338;
    --card: #231f20;
    --green: #22a54a;
  }
  * { margin: 0; padding: 0; box-sizing: border-box; }
  html, body { width: 1200px; height: 960px; overflow: hidden; }
  body {
    background: radial-gradient(ellipse at center, var(--backdrop) 40%, var(--backdrop-edge) 100%);
    display: flex;
    flex-direction: column;
    align-items: center;
    justify-content: center;
    gap: 50px;
    font-family: "Questrial", sans-serif;
    color: var(--green);
  }
  .card {
    position: relative;
    width: 700px;
    height: 400px;
    background: var(--card);
    box-shadow: 0 10px 24px rgba(0,0,0,0.35);
  }
  .brand {
    position: absolute;
    left: 0; right: 0;
    display: flex;
    align-items: center;
    justify-content: center;
    font-family: "Questrial", sans-serif;
    font-weight: 400;
    color: var(--green);
    white-space: nowrap;
  }
  .brand-dot {
    flex: none;
    border-radius: 50%;
    background: var(--green);
  }
  /* back: contact side */
  .card-back .brand { top: 50px; gap: 16px; font-size: 54px; }
  .card-back .brand-dot { width: 30px; height: 30px; }
  .contact {
    position: absolute;
    top: 178px;
    left: 0; right: 0;
    text-align: center;
    line-height: 1.25;
  }
  .contact-name { font-size: 28px; letter-spacing: 1px; }
  .contact-role { font-size: 18px; letter-spacing: 6px; }
  .contact-phone { font-size: 19px; letter-spacing: 0.5px; margin-top: 10px; }
  .contact-site { font-size: 19px; letter-spacing: 0.5px; }
  .tagline {
    position: absolute;
    left: 0; right: 0;
    text-align: center;
    font-family: "Source Sans 3", sans-serif;
    font-size: 21px;
    white-space: nowrap;
  }
  .card-back .tagline { bottom: 30px; }
  /* front: brand side */
  .card-front .brand { top: 110px; gap: 22px; font-size: 80px; }
  .card-front .brand-dot { width: 44px; height: 44px; }
  .card-front .tagline { bottom: 38px; font-size: 24px; }
</style>
</head>
<body>
  <section class="card card-back">
    <div class="brand"><span class="brand-dot"></span><span class="brand-name">Summit Path</span></div>
    <div class="contact">
      <p class="contact-name">Dan Pellow</p>
      <p class="contact-role">Life Coach</p>
      <p class="contact-phone">0468215903</p>
      <p class="contact-site">itsdanp.com.au</p>
    </div>
    <p class="tagline">Life Coach - Professional Adventurer - Entrepreneur</p>
  </section>

  <section class="card card-front">
    <div class="brand"><span class="brand-dot"></span><span class="brand-name">Summit Path</span></div>
    <p class="tagline">Life Coach - Professional Adventurer - Entrepreneur</p>
  </section>
</body>
</html>
```